Website Home Page for Women's Health Medical Office

Redesign existing homepage for website using existing logo. Current website location is www.lumawomenscare.com. Please give it a modern, streamlined, playful feel.

Please give it a feminine feel and make it bright and cheerful using logo colors.

Target Market(s)

Women between the ages of 25-45

Industry/Entity Type

Medical Office

Coding

Coded - Design and coding required

Number of Pages Required

1 page

Font styles to use
Sans Serif
Other font styles liked:
• SEGOI UI script for text and GIL SANS for bold (or their equivilent)

Colors
E54698
E96AAD
F1A4CE
F9D9EA
FCEFF6

Requirements
Must have
• Existing logo. Logo Colors. Feminine, cheerful, simple design. all relevant contact information
Nice to have
• clean lines and streamlined look
Should not have
• Cluttered

```html
<!DOCTYPE html>
<html lang="en">
<head>
<meta charset="utf-8">
<title>Luma OB/GYN – Women's Health Care</title>
<link rel="stylesheet" href="https://fonts.googleapis.com/css2?family=Cabin:wght@400;500;600;700&family=Gloria+Hallelujah&display=swap">
<style>
:root{
  --magenta:#d4106b;
  --pink:#e8388f;
  --pink-mid:#e96aad;
  --pink-soft:#f1a4ce;
  --blush:#f9d9ea;
  --blush-pale:#fdeef5;
  --ink:#1d1d1d;
  --text:#3a3a3a;
  --grey-bg:#f3f3f3;
  --footer:#262626;
  --white:#ffffff;
}
*{box-sizing:border-box;margin:0;padding:0}
html,body{width:1200px;height:4311px;overflow:hidden}
body{position:relative;font-family:"Cabin",sans-serif;color:var(--text);background:var(--white)}
.abs{position:absolute}
.script{font-family:"Gloria Hallelujah",cursive;font-weight:400;color:var(--ink);letter-spacing:2px;text-transform:uppercase}
.script em{font-style:normal;color:var(--pink)}
.btn{display:inline-block;background:var(--pink);color:var(--white);font-weight:700;font-size:14px;letter-spacing:.5px;padding:12px 16px;border-radius:4px;text-transform:uppercase;text-decoration:none}
.placeholder{border-radius:50%}
p{font-size:12.5px;line-height:20px}

/* Header */
.topbar{left:636px;top:16px;display:flex;gap:26px;font-size:14px;font-weight:600;color:var(--ink)}
.topbar span{display:flex;align-items:center;gap:10px}
.topbar i{width:30px;height:30px;border-radius:50%;background:var(--pink);display:flex;align-items:center;justify-content:center}
.nav{left:537px;top:68px;display:flex;gap:22px;font-size:15px;font-weight:700;letter-spacing:.3px;color:var(--ink)}
.brand{left:176px;top:60px;display:flex;align-items:center;gap:10px;z-index:3}
.brand b{font-size:26px;font-weight:700;color:var(--magenta)}
.brand i{width:16px;height:16px;border-radius:50%;background:var(--magenta);display:block}

/* Hero */
.hero{left:0;top:95px;width:1200px;height:825px;overflow:hidden;background:var(--grey-bg)}
.hero-title{left:168px;top:450px;width:540px;color:var(--white);text-align:center;font-size:64px;font-weight:700;line-height:1;letter-spacing:1px}

/* Welcome */
.welcome-title{left:0;top:982px;width:1200px;text-align:center;font-size:32px;line-height:38px}
.welcome-text{left:636px;top:1110px;width:394px;text-align:justify}
.welcome-text p+p{margin-top:10px}

/* Services */
.services{left:0;top:1470px;width:1200px;height:900px;background:var(--blush-pale)}
.services-title{left:0;top:1640px;width:1200px;text-align:center;font-size:33px}
.card{top:1741px;width:236px;height:515px;border-radius:118px;background:var(--white);box-shadow:0 4px 14px rgba(200,40,120,.18);text-align:center;padding:10px 8px 0}
.card .photo{width:220px;height:220px;margin:0 auto}
.card h3{font-size:17.5px;font-weight:500;color:var(--ink);margin:27px 0 14px;letter-spacing:.3px}
.card p{font-size:11.5px;line-height:19.5px;padding:0 4px}
.card .btn{position:absolute;left:32px;right:32px;bottom:-4px;border-radius:0 0 90px 90px;padding:14px 0 18px;font-size:15px}
.card.featured{background:var(--pink)}
.card.featured h3,.card.featured p{color:var(--white)}
.card.featured .btn{background:var(--white);color:var(--ink)}

/* New patients */
.np-title{left:172px;top:2560px;font-size:34px;line-height:50px;width:420px}
.np-sub{left:172px;top:2660px;font-size:21px;color:var(--pink);font-weight:500;letter-spacing:.5px}
.np-text{left:172px;top:2690px;width:390px;text-align:justify}
.np-text p{margin-top:12px}

/* Values */
.values{left:0;top:3095px;width:1200px;height:720px;background:var(--blush-pale)}
.values-title{left:586px;top:3340px;font-size:33px}
.values-list{left:586px;top:3400px;width:444px;list-style:none}
.values-list li{position:relative;padding-left:18px;font-size:12.5px;line-height:19px;margin-bottom:11px;text-align:justify}
.values-list li::before{content:"";position:absolute;left:0;top:5px;border-left:8px solid var(--pink);border-top:5px solid transparent;border-bottom:5px solid transparent}

/* Footer */
.footer{left:0;top:3780px;width:1200px;height:531px;background:var(--footer)}
.contact{left:172px;top:3940px;color:var(--white);font-size:18px;line-height:26px}
.contact .row{display:flex;align-items:center;gap:20px;margin-bottom:22px}
.contact i{width:42px;height:42px;border-radius:50%;background:var(--white);display:flex;align-items:center;justify-content:center;flex:none}
.form{left:619px;top:3912px;width:411px;color:var(--white);font-size:14px;font-weight:600}
.form .grid{display:grid;grid-template-columns:1fr 1fr;gap:0 14px}
.form label{display:block;margin-bottom:6px}
.form .field{height:40px;background:var(--white);border-radius:4px;color:#888;font-size:13px;padding:12px 8px;font-weight:400;margin-bottom:14px}
.form .btn{margin-top:6px;font-size:13px}
.footer-rule{left:172px;top:4230px;width:856px;height:1px;background:#777}
.copyright{left:0;top:4264px;width:1200px;text-align:center;color:var(--white);font-size:14px;font-weight:500}
</style>
</head>
<body>

<!-- Hero -->
<section class="abs hero">
  <svg class="abs" style="left:0;top:0" width="1200" height="825" viewBox="0 0 1200 825">
    <path d="M0 0 H1200 V20 C1000 70 700 150 500 100 C380 70 320 140 340 230 C360 330 480 400 640 420 C760 440 800 560 800 825 H0Z" fill="#d4106b"/>
    <path d="M0 0 H1200 V20 C1000 70 700 150 500 100 C380 70 330 120 320 170 C300 120 260 60 160 60 C80 60 30 50 0 30Z" fill="#fff"/>
    <path d="M0 30 C80 55 200 80 330 95 C500 110 700 60 1200 20" fill="none" stroke="#e8388f" stroke-width="10"/>
  </svg>
  <div class="abs placeholder" role="img" aria-label="Flowers illustration" style="left:750px;top:20px;width:450px;height:230px;background:radial-gradient(circle,#f7b9d5,rgba(247,185,213,0) 70%)"></div>
  <div class="abs" role="img" aria-label="Illustration of a pregnant woman with long pink hair" style="left:780px;top:190px;width:300px;height:635px;border-radius:150px 150px 40px 40px;background:linear-gradient(160deg,#d4106b 0%,#e6569a 45%,#f6c9b5 75%,#f9d3c2 100%)"></div>
  <div class="abs" role="img" aria-label="Leaf illustration" style="left:0;top:530px;width:260px;height:295px;border-radius:0 200px 0 0;background:linear-gradient(45deg,#e9a2a9,rgba(233,162,169,0))"></div>
  <h1 class="abs hero-title">Luma OB/GYN</h1>
</section>

<!-- Header -->
<div class="abs brand"><i></i><b>Luma OB/GYN</b></div>
<div class="abs topbar">
  <span><i><svg width="14" height="14" viewBox="0 0 24 24"><path fill="#fff" d="M6.6 10.8a15 15 0 006.6 6.6l2.2-2.2c.3-.3.7-.4 1-.2 1.1.4 2.3.6 3.6.6.6 0 1 .4 1 1V20c0 .6-.4 1-1 1A17 17 0 013 4c0-.6.4-1 1-1h3.5c.6 0 1 .4 1 1 0 1.3.2 2.5.6 3.6.1.3 0 .7-.2 1z"/></svg></i>(555) 014-2286</span>
  <span><i><svg width="14" height="14" viewBox="0 0 24 24"><rect x="3" y="5" width="18" height="14" rx="2" fill="none" stroke="#fff" stroke-width="2"/><path d="M3 7l9 6 9-6" fill="none" stroke="#fff" stroke-width="2"/></svg></i>admin@lumawomenscare.com</span>
</div>
<nav class="abs nav"><span>HOME</span><span>SERVICES</span><span>RESOURCES</span><span>ABOUT US</span><span>CONTACT US</span></nav>

<!-- Welcome -->
<h2 class="abs script welcome-title">Welcome to <em>Luma OB/GYN,</em><br>Fairhaven, CA</h2>
<div class="abs placeholder" role="img" aria-label="Flower illustration" style="left:1070px;top:975px;width:150px;height:270px;background:radial-gradient(circle,#f0a8c8,rgba(240,168,200,0) 70%)"></div>
<div class="abs" role="img" aria-label="Line illustration of a doctor with a tablet speaking with a female patient" style="left:100px;top:1100px;width:470px;height:320px;border-radius:20px;background:linear-gradient(180deg,#fde7f1,#fbd3e6)"></div>
<div class="abs welcome-text">
  <p>At Luma OB/GYN in Fairhaven, California, we believe better health starts when the patient is educated. For this reason, we take time to listen to our patients concerns, explain each option available, and to answer any questions our patients may have so that they can make informed decisions. At Luma OB/GYN, our providers tailor every procedure performed and treatment option recommended to meet the specific needs of our patients. We remain up-to-date on the latest technology and practice guidelines for women's health.</p>
  <p>Our medical providers will take time to give you the personalized health care you deserve. This includes taking time to listen to you and screening you for problems to help ensure that any health issues are diagnosed and treated as early as possible.</p>
</div>
<a class="abs btn" style="left:636px;top:1373px">Read More</a>

<!-- Services -->
<section class="abs services"></section>
<svg class="abs" style="left:0;top:1460px" width="1200" height="120" viewBox="0 0 1200 120">
  <path d="M0 0 H1200 V20 C1000 0 800 40 600 60 C380 80 200 50 0 10Z" fill="#fff"/>
  <path d="M40 20 C200 70 420 95 600 70 C800 40 1000 5 1200 25" fill="none" stroke="#e8388f" stroke-width="9"/>
</svg>
<div class="abs placeholder" role="img" aria-label="Pink flower illustration" style="left:-40px;top:1580px;width:200px;height:340px;background:radial-gradient(circle,#f294bd,rgba(242,148,189,0) 70%)"></div>
<h2 class="abs script services-title">How can <em>we help you?</em></h2>

<div class="abs card" style="left:109px">
  <div class="photo placeholder" role="img" aria-label="Photo of an expecting couple" style="background:linear-gradient(135deg,#c9b3a4,#6b7f96)"></div>
  <h3>PREGNANCY CARE</h3>
  <p>Receiving regular care in pregnancy is important for the health of both you and your baby. Our obstetricians work with you every step of the way during your pregnancy and delivery to make sure your individual needs are met and co ensure this special journey is a memorable one.</p>
  <a class="btn">Read More</a>
</div>
<div class="abs card featured" style="left:357px">
  <div class="photo placeholder" role="img" aria-label="Photo of a woman holding birth control pills" style="background:linear-gradient(135deg,#5b5b5b,#2f2f2f)"></div>
  <h3>BIRTH CONTROL</h3>
  <p>Our gynecologists are knowledgeable on all forms of birth control including the IUD, arm implants, vaginal ringinsertion, birth control pills, and more! We would love to work with you to determine the best option for you and your lifestyle.</p>
  <a class="btn">Read More</a>
</div>
<div class="abs card" style="left:605px">
  <div class="photo placeholder" role="img" aria-label="Photo of a patient having a mammogram exam" style="background:linear-gradient(135deg,#d8d8d8,#8d8d8d)"></div>
  <h3>WELL WOMAN EXAMS</h3>
  <p>Our providers will help you to stay healthy by performing a physical exam on you annually. We will screen you for multiple health conditions that may pose a risk to you. This includes screening you for cancerous conditions of the breast, ovaries and cervix.</p>
  <a class="btn">Read More</a>
</div>
<div class="abs card" style="left:853px">
  <div class="photo placeholder" role="img" aria-label="Photo of a doctor explaining a model to a patient" style="background:linear-gradient(135deg,#ece4dc,#b9a493)"></div>
  <h3>WOMEN'S HEALTH</h3>
  <p>Whether you are dealing with painful or irregular periods, fibroids, or other women's health i ssues, we can help. We offer a variety of the most up-to-date treatment options to help you regain your lifestyle.</p>
  <a class="btn">Read More</a>
</div>

<svg class="abs" style="left:0;top:2300px" width="1200" height="140" viewBox="0 0 1200 140">
  <path d="M0 40 C200 110 420 110 620 80 C850 45 1000 15 1200 35 V140 H0Z" fill="#fff"/>
  <path d="M0 40 C200 110 420 110 620 80 C850 45 1000 15 1200 35" fill="none" stroke="#e8388f" stroke-width="9"/>
</svg>

<!-- New patients -->
<h2 class="abs script np-title">Now accepting <em>new patients</em></h2>
<div class="abs np-sub">YOUR OB/GYN SPECIALISTS</div>
<div class="abs np-text">
  <p>Luma OB/GYN offers you the best care possible in a personalized setting. We are currently accepting patients. Call our office now to make an appointment.</p>
  <p>Luma OB/GYN (located near Fairhaven Springs Hospital in Fairhaven, CA) is a medical office that specializes in Christ-centered healthcare for women of all ages. Our team of exclusively female providers have years of experience taking care of women with a variety of pregnancy and gynecology concerns.</p>
  <p>Whether you need a routine examination, help during your pregnancy, have questions on birth control, or another female concern, we offer the best care possible for our patients. That is why better health starts here.</p>
</div>
<a class="abs btn" style="left:172px;top:2953px">Read More</a>
<div class="abs placeholder" role="img" aria-label="Pink flower behind the portrait" style="left:605px;top:2560px;width:500px;height:520px;background:radial-gradient(circle,#f3b7cf 0%,#f7cfe0 55%,rgba(247,207,224,0) 72%)"></div>
<div class="abs" role="img" aria-label="Photo of a smiling pregnant woman holding her belly" style="left:720px;top:2392px;width:260px;height:680px;border-radius:130px 130px 40px 40px;background:linear-gradient(180deg,#8a5a42 0%,#e8c2ad 25%,#f3f0ee 45%,#e8c2ad 62%,#4d6c8f 80%,#3e5b7c 100%)"></div>

<!-- Values -->
<section class="abs values"></section>
<svg class="abs" style="left:0;top:3085px" width="1200" height="120" viewBox="0 0 1200 120">
  <path d="M0 0 H1200 V30 C1000 15 780 45 560 75 C360 100 180 80 0 20Z" fill="#fff"/>
  <path d="M20 30 C200 90 400 105 600 80 C820 50 1000 25 1200 35" fill="none" stroke="#e8388f" stroke-width="9"/>
</svg>
<div class="abs placeholder" role="img" aria-label="Pink floral watercolor" style="left:-20px;top:3560px;width:380px;height:260px;background:radial-gradient(circle,#f6bfd6,rgba(246,191,214,0) 70%)"></div>
<div class="abs placeholder" role="img" aria-label="Photo of two smiling medical staff members" style="left:167px;top:3315px;width:340px;height:340px;border:6px solid #fff;background:linear-gradient(135deg,#a8928a,#4c4140)"></div>
<div class="abs placeholder" role="img" aria-label="Portrait photo of a smiling doctor in navy scrubs" style="left:218px;top:3490px;width:240px;height:240px;border:6px solid #fff;background:linear-gradient(180deg,#6d6a76,#1f2a48)"></div>
<h2 class="abs script values-title">Our <em>core values</em></h2>
<ul class="abs values-list">
  <li>We believe that every person's mission is to shine the light of Christ by showing kindness and compassion to others.</li>
  <li>We believe that every woman should have personalized high-quality medical in all stages of their lives.</li>
  <li>We believe that it is important to develop lifelong relationships with our patients by listening to their needs and providing honest, straight-forward medical advice.</li>
  <li>We strive to be fair, honest and ethical in all dealings with our patients, employees, other physicians and anyone else we encounter.</li>
  <li>We vow to practice evidence-based medicine and utilize innovative technology when treating our patients.</li>
  <li>We stive to be a great place to work.</li>
</ul>

<!-- Footer -->
<section class="abs footer"></section>
<svg class="abs" style="left:0;top:3740px" width="1200" height="110" viewBox="0 0 1200 110">
  <path d="M0 0 H1200 V20 C1000 0 800 20 600 45 C400 70 200 75 0 55Z" fill="#fdeef5"/>
  <path d="M0 55 C200 75 400 70 600 45 C800 20 1000 0 1200 20" fill="none" stroke="#e8388f" stroke-width="9"/>
</svg>
<div class="abs placeholder" role="img" aria-label="Pink floral watercolor" style="left:900px;top:3740px;width:320px;height:230px;background:radial-gradient(circle,#e77fae,rgba(231,127,174,0) 70%)"></div>
<div class="abs contact">
  <div class="row"><i><svg width="20" height="20" viewBox="0 0 24 24"><path d="M12 2a7 7 0 00-7 7c0 5 7 13 7 13s7-8 7-13a7 7 0 00-7-7z" fill="none" stroke="#262626" stroke-width="2"/><circle cx="12" cy="9" r="2.5" fill="#262626"/></svg></i><span>1840 Willow Crest Avenue, Suite 210,<br>Fairhaven, CA 90210</span></div>
  <div class="row"><i><svg width="20" height="20" viewBox="0 0 24 24"><path fill="none" stroke="#262626" stroke-width="2" d="M6.6 10.8a15 15 0 006.6 6.6l2.2-2.2c.3-.3.7-.4 1-.2 1.1.4 2.3.6 3.6.6.6 0 1 .4 1 1V20c0 .6-.4 1-1 1A17 17 0 013 4c0-.6.4-1 1-1h3.5c.6 0 1 .4 1 1 0 1.3.2 2.5.6 3.6.1.3 0 .7-.2 1z"/></svg></i><span>(555) 014-2286<br>(555) 014-2290</span></div>
  <div class="row"><i><svg width="20" height="20" viewBox="0 0 24 24"><rect x="3" y="5" width="18" height="14" rx="2" fill="none" stroke="#262626" stroke-width="2"/><path d="M3 7l9 6 9-6" fill="none" stroke="#262626" stroke-width="2"/></svg></i><span>admin@lumawomenscare.com</span></div>
</div>
<div class="abs form">
  <label>Name *</label>
  <div class="grid"><div class="field">First</div><div class="field">Last</div></div>
  <div class="grid"><label>Email Address *</label><label>Phone *</label><div class="field"></div><div class="field"></div></div>
  <label>Phone *</label>
  <div class="field"></div>
  <a class="btn">Submit Query</a>
</div>
<div class="abs footer-rule"></div>
<div class="abs copyright">Copyrights @ 2022 Luma. All Rights Reserved.</div>

</body>
</html>
```